VMR business card

Need a business card for a company that provides instructional design and elearning development services. The website is here: http://vantmoro.studio/

I'm attaching a current logo, as well as the old business card design. While I like to keep it clean, the old design is too simplistic for my liking. The only idea I want to reuse from the old design is placing industry jargon on the back of the card, just need a better way to present it. But if you have other ideas for the back--feel free to experiment.

Please use the colors complementary to the color we have on the website. Thank you!

```html
<!DOCTYPE html>
<html lang="en">
<head>
<meta charset="utf-8">
<title>VMR business card</title>
<link href="https://fonts.googleapis.com/css2?family=Mulish:wght@400;600;700&family=Lato:wght@700&display=swap" rel="stylesheet">
<style>
  :root {
    --stage: #231f20;
    --paper: #ffffff;
    --teal: #26b0b0;
    --teal-soft: rgba(38, 176, 176, 0.55);
    --teal-fade: rgba(38, 176, 176, 0);
    --ink: #111111;
    --ink-soft: #333333;
    --icon: #777777;
  }
  * { box-sizing: border-box; margin: 0; padding: 0; }
  html, body { width: 1200px; height: 898px; overflow: hidden; background: var(--stage); }
  .canvas { position: relative; width: 1200px; height: 898px; }

  .card { position: absolute; width: 512px; height: 301px; overflow: hidden; }
  .card--front { background: var(--paper); left: 65px; }
  .card--back { left: 611px; }
  .row-one { top: 108px; }
  .row-two { top: 470px; }
  .card--back-plain { background: var(--teal); }
  .card--back-panel { background: var(--paper); }

  .brand {
    position: absolute; display: flex; align-items: center; gap: 10px;
    font-family: "Mulish", sans-serif; font-weight: 700; font-size: 34px;
    color: var(--teal); letter-spacing: 1px; line-height: 1;
  }
  .brand__mark { width: 22px; height: 22px; border-radius: 50%; background: var(--teal); }
  .row-one .brand { left: 231px; top: 32px; }
  .row-two .brand { left: 24px; top: 34px; }

  .holder { position: absolute; left: 231px; top: 134px; }
  .holder__name {
    font-family: "Lato", sans-serif; font-weight: 700; font-size: 24px; color: var(--ink);
    line-height: 1.1;
  }
  .holder__role {
    font-family: "Mulish", sans-serif; font-size: 17px; color: var(--ink-soft); margin-top: 3px;
  }
  .contacts { list-style: none; margin-top: 16px; }
  .contacts__item {
    display: flex; align-items: center; gap: 7px; height: 23px;
    font-family: "Mulish", sans-serif; font-size: 13px; color: var(--ink-soft);
  }
  .contacts__icon { width: 15px; height: 15px; flex: none; }

  .web {
    position: absolute; font-family: "Mulish", sans-serif; font-weight: 700;
    color: var(--paper); white-space: nowrap; transform: translate(-50%, -50%);
  }
  .card--back-plain .web { left: 50%; top: 149px; font-size: 20px; }
  .card--back-panel .web { left: 368px; top: 150px; font-size: 17px; }
  .panel { position: absolute; inset: 0; width: 512px; height: 301px; }
  .decor-area {
    position: absolute; left: 0; top: 70px; width: 240px; height: 210px;
    background: radial-gradient(ellipse at 45% 50%, var(--teal-soft) 0%, var(--teal-fade) 70%);
  }
</style>
</head>
<body>
<main class="canvas">

  <section class="card card--front row-one">
    <div class="brand"><span class="brand__mark"></span>VMR</div>
    <div class="holder">
      <p class="holder__name">Daniel Marlowe</p>
      <p class="holder__role">Director</p>
      <ul class="contacts">
        <li class="contacts__item">
          <svg class="contacts__icon" viewBox="0 0 16 16"><circle cx="8" cy="8" r="7" fill="none" stroke="var(--icon)" stroke-width="1.2"/><path d="M5.5 4.5c-.6.6-.5 2 .8 3.6s2.8 2.4 3.6 1.8l.6-.6-1.4-1.2-.7.5c-.5-.2-1.5-1.2-1.7-1.7l.5-.7-1.2-1.4z" fill="var(--icon)"/></svg>
          555 - 014 - 2837
        </li>
        <li class="contacts__item">
          <svg class="contacts__icon" viewBox="0 0 16 16"><circle cx="8" cy="8" r="7" fill="none" stroke="var(--icon)" stroke-width="1.2"/><rect x="4.5" y="5.5" width="7" height="5" fill="none" stroke="var(--icon)" stroke-width="1"/><path d="M4.5 5.5 8 8.4l3.5-2.9" fill="none" stroke="var(--icon)" stroke-width="1"/></svg>
          dmarlowe@vantmoro.studio
        </li>
      </ul>
    </div>
  </section>

  <section class="card card--back card--back-plain row-one">
    <p class="web">www.vantmoro.studio</p>
  </section>

  <section class="card card--front row-two">
    <div class="brand"><span class="brand__mark"></span>VMR</div>
    <div class="holder">
      <p class="holder__name">Daniel Marlowe</p>
      <p class="holder__role">Director</p>
      <ul class="contacts">
        <li class="contacts__item">
          <svg class="contacts__icon" viewBox="0 0 16 16"><circle cx="8" cy="8" r="7" fill="none" stroke="var(--icon)" stroke-width="1.2"/><path d="M5.5 4.5c-.6.6-.5 2 .8 3.6s2.8 2.4 3.6 1.8l.6-.6-1.4-1.2-.7.5c-.5-.2-1.5-1.2-1.7-1.7l.5-.7-1.2-1.4z" fill="var(--icon)"/></svg>
          555 - 014 - 2837
        </li>
        <li class="contacts__item">
          <svg class="contacts__icon" viewBox="0 0 16 16"><circle cx="8" cy="8" r="7" fill="none" stroke="var(--icon)" stroke-width="1.2"/><rect x="4.5" y="5.5" width="7" height="5" fill="none" stroke="var(--icon)" stroke-width="1"/><path d="M4.5 5.5 8 8.4l3.5-2.9" fill="none" stroke="var(--icon)" stroke-width="1"/></svg>
          dmarlowe@vantmoro.studio
        </li>
      </ul>
    </div>
  </section>

  <section class="card card--back card--back-panel row-two">
    <div class="decor-area" role="img" aria-label="Decorative cluster of teal geometric shapes"></div>
    <svg class="panel" viewBox="0 0 427 251" aria-hidden="true">
      <polygon points="257,0 427,0 427,251 251,251 181,133" fill="var(--teal)"/>
    </svg>
    <p class="web">www.vantmoro.studio</p>
  </section>

</main>
</body>
</html>
```